Digital Price Menus for Detail Shop

I am looking to have digital menus for my detail shop. I have 3 55-inch TVs (see pictures) on how they are situated on the wall for my front desk area. They will be vertical, not horizontal.

Color pallet I am looking for is black and gold, with some accent colors if applicable. I would like black background with some sort of design in it in such a way it looks faint or ghosted in the background ... i.e., honeycomb, splatter, etc. A boarder is optional.

Needs to be designed well, organized well and easy to read for customers walking in.

the each document is for each TV, Interior, Exterior and Ceramic Coatings

Company logo files included. would like my logos on them as well

Target Market(s)

Customers walking in to my shop, easy to read and understand

Industry/Entity Type

Car wash, Detailing

Colors

Designer to choose only greyscale colors for use in the design.

Requirements
Nice to have
• Professional Look
Should not have
• tacky look

```html
<!DOCTYPE html>
<html lang="en">
<head>
<meta charset="utf-8">
<title>Luster Garage – Service Menus</title>
<link rel="stylesheet" href="https://fonts.googleapis.com/css2?family=Bebas+Neue&family=Montserrat:wght@400;500;600;700;800&display=swap">
<style>
:root{
  --page:#ffffff;
  --black:#070707;
  --panel:#0d0d0d;
  --gold:#c8a548;
  --gold-light:#e4c768;
  --gold-dark:#8a6d22;
  --white:#f4f4f4;
  --grey:#cfcfcf;
  --ink:#151515;
}
*{box-sizing:border-box;margin:0;padding:0}
html,body{width:901px;height:1200px;overflow:hidden;background:var(--page)}
body{font-family:"Montserrat",sans-serif;color:var(--white)}
.menu-row{position:absolute;top:349px;left:10px;width:881px;display:flex;justify-content:space-between}
.menu{position:relative;width:283px;height:502px;overflow:hidden;text-align:center;
  background:radial-gradient(ellipse at 50% 40%,#1a1a1a 0%,var(--panel) 60%,var(--black) 100%)}
.menu-texture{position:absolute;inset:0;background:linear-gradient(160deg,rgba(255,255,255,.035),rgba(255,255,255,0) 60%)}
.corner-bands{position:absolute;top:0;left:0;width:283px;height:70px}
.blk{position:absolute}
.brand{top:18px;left:0;width:100%;display:flex;flex-direction:column;align-items:center;gap:6px}
.brand-dot{width:16px;height:16px;border-radius:50%;background:var(--white)}
.brand-name{font-weight:700;font-size:9px;letter-spacing:.6px;color:var(--white)}
.title-band{top:73px;left:0;width:100%;height:30px;border-bottom:1px solid var(--gold-dark);display:flex;justify-content:center}
.title-ribbon{height:28px;padding:0 20px;background:linear-gradient(180deg,var(--gold-light),var(--gold));
  clip-path:polygon(0 0,100% 0,93% 100%,7% 100%);
  font-family:"Bebas Neue",sans-serif;font-size:17px;line-height:30px;color:var(--ink);white-space:nowrap}
.gold{color:var(--gold-light)}
.gold-box{background:linear-gradient(180deg,var(--gold-light),var(--gold));color:var(--ink);border-radius:4px}
.tier-name{font-size:8.4px;font-weight:500;color:var(--gold-light);line-height:10px;text-transform:uppercase}
.bracket{border:1px solid var(--gold);border-bottom:none;height:12px;margin:2px 3px 0}
.price{font-size:8.4px;font-weight:700;line-height:11px;margin-top:-8px}
.and-up{font-size:4.4px;font-weight:700;line-height:5px}
.fine{font-size:4.2px;line-height:5.3px;color:var(--grey);margin-top:3px}
.fine.w{color:var(--white)}
.note{font-size:4.6px;font-weight:700;color:var(--gold-light);line-height:6px}
/* exterior */
.ask{font-size:8.2px;font-weight:800;line-height:10px;text-align:left}
.ask .soft{font-weight:500}
.restore{top:317px;left:18px;width:247px;height:45px;padding:21px 12px 0;clip-path:polygon(2% 0,98% 0,100% 100%,0 100%)}
.restore-tag{position:absolute;top:0;left:50%;transform:translateX(-50%);background:var(--panel);color:var(--white);
  font-size:7.6px;font-weight:800;line-height:13px;padding:0 18px;white-space:nowrap;clip-path:polygon(0 0,100% 0,93% 100%,7% 100%)}
.restore p{font-size:4.7px;line-height:5.8px}
.addons-head{top:372px;left:0;width:100%;font-size:5.4px;font-weight:800}
.addons{top:383px;left:14px;width:255px;display:flex;gap:3px}
.addon{flex:1}
.addon h4{font-size:6.6px;font-weight:500;color:var(--gold-light);line-height:7.2px}
.dots{font-size:5px;letter-spacing:1px;line-height:6px}
.addon .p{font-size:7px;line-height:8px}
.addon .p b{color:var(--gold-light)}
.line-item{left:20px;width:243px;display:flex;align-items:center;text-align:left;gap:8px}
.line-item h5{width:50%;font-size:6.6px;font-weight:500;color:var(--gold-light);line-height:7.4px}
.line-item p{width:50%;font-size:4px;line-height:5px}
.line-item p.big{font-size:7px;line-height:8px}
/* ceramic */
.intro{top:110px;left:36px;width:211px;font-size:6.4px;line-height:11px}
.callout{top:201px;left:26px;width:231px;height:30px;padding:3px 8px;font-size:6.1px;line-height:8px;font-weight:500}
.coatings{top:248px;left:16px;width:251px;display:flex;gap:5px}
.coat{flex:1}
.coat h3{font-size:8.8px;font-weight:700;color:var(--gold-light);line-height:10px}
.coat .sub{font-size:5px;font-weight:600;line-height:6px}
.coat .bracket{height:14px;margin-top:1px}
.coat .from{font-size:5.2px;font-weight:700;margin-top:-8px;line-height:7px}
.coat .amt{font-size:9px;font-weight:700;color:var(--gold-light);line-height:11px}
.coat .fine{font-size:4.6px;line-height:5.8px;margin-top:2px}
.durability{top:345px;left:26px;width:231px;border:1px solid var(--gold);height:16px;font-size:5.4px;line-height:14px;font-weight:600}
.glass{top:366px;left:0;width:100%;font-size:7.4px;font-weight:800;line-height:9px}
.glass span{color:var(--white)}
.extras{top:396px;left:26px;width:231px;display:flex;gap:26px}
.extras>div{flex:1}
.extras .tier-name{font-size:8px}
.extras .price{font-size:7px;line-height:9px;margin-top:-6px}
.extras .fine{font-size:4.6px;line-height:5.8px;margin-top:8px}
/* interior */
.reminder{top:106px;left:20px;width:243px;font-size:6.8px;line-height:8.6px}
.reminder-sm{left:20px;width:243px;font-size:5.2px;line-height:6.6px}
.link{top:157px;left:0;width:100%;font-size:5.2px;font-weight:700;color:var(--gold-light)}
.wide{left:16px;width:251px}
.wide .frame{border:1px solid var(--gold);border-bottom:none;height:14px}
.wide .tab{position:absolute;top:-5px;left:50%;transform:translateX(-50%);background:var(--panel);padding:0 8px;font-size:7.2px;font-weight:800;color:var(--gold-light);white-space:nowrap;line-height:10px}
.wide .tab span{color:var(--white)}
.wide .p{font-size:8.6px;font-weight:500;margin-top:-6px;line-height:10px}
.wide .p b{color:var(--gold-light);font-weight:700}
.wide .fine{color:var(--white);font-size:4.8px;line-height:6px;margin-top:2px}
.wide .note{font-size:4.8px;margin-top:1px}
.pair{left:18px;width:247px;display:flex;gap:14px}
.pair>div{flex:1}
.pair .tier-name{font-size:6.6px;font-weight:700;line-height:8px}
.pair .bracket{height:14px}
.pair .p{font-size:11px;font-weight:500;margin-top:-9px;line-height:13px}
.pair .p b{color:var(--gold-light);font-weight:700}
.pair .fine{font-size:4.8px;line-height:5.8px;margin-top:1px}
.surcharge{top:452px;left:28px;width:227px;height:19px;font-family:"Bebas Neue",sans-serif;font-size:11px;line-height:20px;color:var(--ink)}
.trunk{top:476px;left:0;width:100%;font-size:8px;font-weight:600;color:var(--gold-light)}
.trunk span{color:var(--white)}
</style>
</head>
<body>
<div class="menu-row">

  <!-- EXTERIOR -->
  <section class="menu menu-exterior">
    <div class="menu-texture"></div>
    <svg class="corner-bands" viewBox="0 0 283 70" aria-hidden="true">
      <polygon points="0,0 22,0 60,42 0,42" fill="#2a2410"/>
      <polygon points="0,0 14,0 48,38 34,38" fill="#c8a548"/>
      <polygon points="283,0 261,0 223,42 283,42" fill="#2a2410"/>
      <polygon points="283,0 269,0 235,38 249,38" fill="#c8a548"/>
    </svg>
    <div class="blk brand"><span class="brand-dot"></span><span class="brand-name">LUSTER GARAGE</span></div>
    <div class="blk title-band"><div class="title-ribbon">EXTERIOR DETAILING PACKAGES</div></div>

    <div class="blk tier" style="top:115px;left:22px;width:115px">
      <div class="tier-name">Hand Wash</div>
      <div class="bracket"></div>
      <div class="price">Cars <span class="gold">$50</span><br>Trucks/SUVS <span class="gold">$60</span></div>
      <div class="and-up">and up</div>
      <p class="fine">Presoak, foam bath, bug remover, wheel detail, wheel wells cleaned, tires dressed, exterior glass cleaned, blow dry (+add spray wax $20)</p>
    </div>
    <div class="blk tier" style="top:106px;left:148px;width:115px">
      <div class="tier-name">Complete Exterior<br>Detail</div>
      <div class="bracket"></div>
      <div class="price">Cars <span class="gold">$180</span><br>Trucks/SUVS <span class="gold">$220</span></div>
      <p class="fine">Standard hand wash, iron decontamination, clay bar treatment to remove environmental contamination (sap, tar, etc), tires, wheels, wheel wells cleaned and dressed, door jams, trunk lid, gas cap areas cleaned, exterior glass cleaned, black plastics dressed, Paint work is protected with a hand applied wax</p>
    </div>

    <div class="blk ask" style="top:196px;left:24px;width:120px"><span class="gold">NEED SCRATCHES</span> <span class="gold soft">and</span><br>SWIRLS REMOVED?</div>
    <p class="blk note" style="top:208px;left:148px;width:115px">DOES NOT REMOVE ANY PAINT DEFECTS</p>

    <div class="blk tier" style="top:223px;left:22px;width:115px">
      <div class="tier-name">Paint<br>Enhancement</div>
      <div class="bracket"></div>
      <div class="price">Cars <span class="gold">$350</span><br>Trucks/SUVs <span class="gold">$400</span></div>
      <p class="fine">Our paint protection package PLUS paint receives a one-step polish to deep clean the paint, reduce swirls and increases gloss, windshield is polished and protected with AquaBead, Paint work is protected with a Ceramic Sealant lasting up to 6 months.</p>
    </div>
    <div class="blk tier" style="top:223px;left:148px;width:115px">
      <div class="tier-name">Paint<br>Correction</div>
      <div class="bracket"></div>
      <div class="price">Cars <span class="gold">$500</span><br>Trucks/SUVs <span class="gold">$600</span></div>
      <p class="fine">Our paint enhancement PLUS paint receives a 2-step correction process to safely remove swirls, defects, and minor scratches, achieving 90% or better appearance</p>
    </div>

    <div class="blk restore gold-box">
      <span class="restore-tag">RESTORATIVE DETAIL</span>
      <p>Our paint protection package PLUS paint receives a one-step polish to deep clean the paint, reduce swirls and increases gloss, windshield is polished and protected with AquaBead, Paint work is protected with a Ceramic Sealant lasting up to 6 months.</p>
    </div>

    <div class="blk addons-head">EXTERIOR ADD-ONS</div>
    <div class="blk addons">
      <div class="addon"><h4>COMPLETE<br>WHEEL DETAIL</h4><div class="dots">•••</div><p class="fine w">Wheels off, deep cleaned and protected inside and out, reinstalled and torqued to factory spec: $150</p></div>
      <div class="addon"><h4>SCRATCH<br>REMOVAL</h4><div class="dots">•••</div><p class="fine w">Consultation required before job</p></div>
      <div class="addon"><h4>HEADLIGHT<br>RESTORATION</h4><div class="dots">•••</div><p class="p"><b>$100</b><br>and up</p></div>
      <div class="addon"><h4>PLASTIC TRIM<br>RESTORATION</h4><div class="dots">•••</div><p class="p"><b>$50</b><br>and up</p></div>
    </div>

    <div class="blk line-item" style="top:440px"><h5>WATER SPOT REMOVAL</h5><p class="big"><span class="gold">$50</span> and up</p></div>
    <div class="blk line-item" style="top:455px"><h5>BRIGHTPANE WINDOW<br>PROTECTION</h5><p>$100/Windshield, $150 all windows: Glass surface(s) prepped and polished, 3-year warrantied protection plan with quarterly maintenance for free</p></div>
    <div class="blk line-item" style="top:478px"><h5>ENGINE BAY CLEANING</h5><p>$50 and up: Degreased and dressed. Waiver MUST BE signed and completed prior to work being performed</p></div>
  </section>

  <!-- CERAMIC -->
  <section class="menu menu-ceramic">
    <div class="menu-texture"></div>
    <svg class="corner-bands" viewBox="0 0 283 70" aria-hidden="true">
      <polygon points="0,0 22,0 60,42 0,42" fill="#2a2410"/>
      <polygon points="0,0 14,0 48,38 34,38" fill="#c8a548"/>
      <polygon points="283,0 261,0 223,42 283,42" fill="#2a2410"/>
      <polygon points="283,0 269,0 235,38 249,38" fill="#c8a548"/>
    </svg>
    <div class="blk brand"><span class="brand-dot"></span><span class="brand-name">LUSTER GARAGE</span></div>
    <div class="blk title-band"><div class="title-ribbon">CERAMIC COATINGS</div></div>

    <p class="blk intro">All ceramic coating packages start with a Paint enhancement package. The 1 step polish will improve the appearance of blemishes, light marring and scratching 50-70%. On new cars it will reach up to 95%+ improvement. A full paint correction can be added for an additional cost. Day of pick up, a Sealant is applied to all coated surfaces to help with the curing process.</p>
    <p class="blk callout gold-box">Not every customer has the same goals when it comes to coatings so we have developed 3 different levels to choose from depending on your wants and needs and budget.</p>

    <div class="blk coatings">
      <div class="coat"><h3>1 YEAR</h3><div class="sub">COATING</div><div class="bracket"></div><div class="from">Starting at</div><div class="amt">$500</div><p class="fine w">applied to all painted surfaces, provides up to 12months of durability. Add a second layer for $600 more for 18-24 months of protection</p></div>
      <div class="coat"><h3>3 YEAR</h3><div class="sub">COATING</div><div class="bracket"></div><div class="from">Starting at</div><div class="amt">$800</div><p class="fine w">applied to all painted surfaces, provides up to 36 months of durability</p></div>
      <div class="coat"><h3>5 YEAR</h3><div class="sub">COATING</div><div class="bracket"></div><div class="from">Starting at</div><div class="amt">$1000</div><p class="fine w">Starting at $1000, warrantied paint coating, applied to all painted surfaces, provides up to 60 months of durability</p></div>
    </div>

    <p class="blk durability">Durability is directly related to the proper maintenance of the coatings</p>
    <p class="blk glass gold">GLASS CERAMIC COATING &nbsp;<span>STARTING AT $100</span></p>

    <div class="blk extras">
      <div><div class="tier-name">Wheel Face<br>Coating</div><div class="bracket"></div><div class="price"><span class="gold">$100</span>/Windshield<br><span class="gold">$150</span> all windows:</div><p class="fine w">Glass surface(s) prepped and polished. 3-year warrantied protection plan with quarterly maintenance for free</p></div>
      <div><div class="tier-name">Engine Bay<br>Cleaning</div><div class="bracket"></div><div class="price"><span class="gold">$50</span> and up</div><p class="fine w" style="margin-top:17px">Degreased and dressed. Waiver MUST BE signed and completed prior to work being performed</p></div>
    </div>
  </section>

  <!-- INTERIOR -->
  <section class="menu menu-interior">
    <div class="menu-texture"></div>
    <svg class="corner-bands" viewBox="0 0 283 70" aria-hidden="true">
      <polygon points="0,0 22,0 60,42 0,42" fill="#2a2410"/>
      <polygon points="0,0 14,0 48,38 34,38" fill="#c8a548"/>
      <polygon points="283,0 261,0 223,42 283,42" fill="#2a2410"/>
      <polygon points="283,0 269,0 235,38 249,38" fill="#c8a548"/>
    </svg>
    <div class="blk brand"><span class="brand-dot"></span><span class="brand-name">LUSTER GARAGE</span></div>
    <div class="blk title-band"><div class="title-ribbon">INTERIOR DETAIL PACKAGES</div></div>

    <p class="blk reminder">As a reminder, we would appreciate all personal items be removed from interior</p>
    <p class="blk reminder-sm" style="top:127px">There may be instances were stains and pet hair are not fully removed, please understand we will do our best to remove as much as possible</p>
    <p class="blk reminder-sm" style="top:147px">Please see terms and conditions</p>
    <p class="blk link">https://www.lustergarage.com/terms-and-conditions</p>

    <div class="blk wide" style="top:176px">
      <div class="frame"></div><div class="tab">BASIC <span>INTERIOR CLEAN</span></div>
      <p class="p"><b>$100</b> and up</p>
      <p class="fine">Full vacuum of carpet, seats, upholstery, Floormats extracted and steam cleaned, dash/doors wiped and dressed, interior glass surfaces cleaned, center console steam cleaned</p>
    </div>
    <div class="blk wide" style="top:233px">
      <div class="frame"></div><div class="tab">DELUX <span>INTERIOR CLEAN</span></div>
      <p class="p"><b>$100</b> and up</p>
      <p class="fine">Basic interior package + Full steam clean and shampoo of all interior carpet and seats, leather is gently steamed and scrubbed lightly, dash/doors/vents are dusted and dressed, steering wheel and controls are deep cleaned and dressed. Headliner/visors are lightly cleaned</p>
      <p class="note">Heavily soiled interiors that exceed a Deluxe Package will be charged extra</p>
    </div>

    <div class="blk pair" style="top:310px">
      <div><div class="tier-name">Deep Leather Cleaning<br>and Conditioning</div><div class="bracket"></div><p class="p"><b>$100</b> per row</p><p class="fine w">Deluxe interior package + premium leather conditioning treatment</p></div>
      <div><div class="tier-name">Ozone Treatment<br>for Odors</div><div class="bracket"></div><p class="p"><b>$100</b> per row</p><p class="fine w">Deluxe interior package + premium leather conditioning treatment</p></div>
    </div>
    <div class="blk pair" style="top:380px">
      <div><div class="tier-name" style="margin-top:8px">Fabric Guard</div><div class="bracket"></div><p class="p"><b>$100</b> per row</p><p class="fine w">Carpet and Fabric upholstery sprayed for stain and waterproofing</p></div>
      <div><div class="tier-name">Biohazard<br>Cleaning</div><div class="bracket"></div><p class="p"><b>$350</b></p><p class="fine w" style="margin-top:3px">Plus Deluxe Interior Package</p></div>
    </div>

    <p class="blk surcharge gold-box">EXCESSIVE PET HAIR REMOVAL: 10% SURCHARGE OF TOTAL</p>
    <p class="blk trunk">TRUNK AREA DETAIL : $50 <span>AND UP</span></p>
  </section>

</div>
</body>
</html>
```